Kolvane Business Card

Require a business card for KolVane. KolVane is an aircraft engineering consultancy company.
Company is used for end of leases inspections, pre purchase inspections,asset inspections

Industry/Entity Type

Business

Contact Information for Business Card

KolVane Limited
Rhys Palgrave
rhys@kolvane.example
64 (0)215580392

Requirements
Must have
• Aircraft silhouette in background

```html
<!DOCTYPE html>
<html lang="en">
<head>
<meta charset="utf-8">
<title>KolVane Business Card</title>
<link href="https://fonts.googleapis.com/css2?family=Open+Sans:wght@400;700;800&display=swap" rel="stylesheet">
<style>
  :root {
    --brand-green: #159a1c;
    --brand-green-light: #3bb043;
    --card-white: #ffffff;
    --backdrop: #e6e6e6;
    --text-on-green: #ffffff;
  }
  * { margin: 0; padding: 0; box-sizing: border-box; }
  html, body {
    width: 1200px;
    height: 810px;
    overflow: hidden;
    background: var(--backdrop);
    font-family: "Open Sans", Arial, sans-serif;
  }
  .business-card {
    position: absolute;
    left: 75px;
    top: 105px;
    width: 1050px;
    height: 600px;
    background: var(--card-white);
    overflow: hidden;
    box-shadow: 0 6px 24px rgba(0,0,0,0.18);
  }
  .aircraft-silhouette {
    position: absolute;
    left: 300px;
    top: 24px;
    width: 720px;
    height: 300px;
    border-radius: 40px;
    background: radial-gradient(ellipse at 65% 45%, var(--brand-green-light) 0%, var(--brand-green) 55%, rgba(21,154,28,0.15) 100%);
    opacity: 0.9;
  }
  .company-name {
    position: absolute;
    left: 64px;
    top: 215px;
    font-weight: 800;
    font-size: 64px;
    letter-spacing: 1px;
    color: var(--brand-green);
  }
  .name-tab {
    position: absolute;
    left: 330px;
    top: 312px;
    width: 230px;
    height: 52px;
    background: var(--brand-green);
  }
  .name-box {
    position: absolute;
    left: 60px;
    top: 360px;
    width: 500px;
    height: 78px;
    background: var(--brand-green);
  }
  .person-name {
    position: absolute;
    left: 84px;
    top: 366px;
    font-weight: 700;
    font-size: 46px;
    color: var(--text-on-green);
  }
  .contact-details {
    position: absolute;
    left: 88px;
    top: 450px;
    font-size: 21px;
    line-height: 30px;
    color: var(--brand-green);
  }
  .stripe-thin {
    position: absolute;
    left: 0;
    width: 100%;
    height: 7px;
    background: var(--brand-green);
  }
  .stripe-thin.upper { top: 518px; }
  .stripe-thin.lower { top: 586px; }
  .stripe-band {
    position: absolute;
    left: 0;
    top: 535px;
    width: 100%;
    height: 42px;
    background: var(--brand-green);
  }
</style>
</head>
<body>
  <div class="business-card">
    <div class="aircraft-silhouette" role="img" aria-label="Green silhouette of a jet airliner taking off, wheels down"></div>
    <div class="company-name">KolVane</div>
    <div class="name-tab"></div>
    <div class="name-box"></div>
    <div class="person-name">Rhys Palgrave</div>
    <div class="contact-details">
      <p>64 (0)215580392</p>
      <p>rhys@kolvane.example</p>
    </div>
    <div class="stripe-thin upper"></div>
    <div class="stripe-band"></div>
    <div class="stripe-thin lower"></div>
  </div>
</body>
</html>
```